Book Cover - Goals

Create book cover for book
Title: Summit Drive
Subtitle: Push Past Your Limits, Find Strength Within Yourself

See the uploaded 1st version -- I want to see different concepts -- definitely want use white space and keep a blue color similiar if not the same as the one seen in that other version and see my notes/feedback.

:

Target Market(s)

Women + Men - 35-60
Self Help + Health

Industry/Entity Type

Health And Wellness

Font styles to use
Sans Serif

Colors
0692cd
34a7d7
85cae6
cee9f5

Requirements
Must have
• Picture of father and I that can be found here:(https://files.cloudvault-share.net/folders/7K9QxRm2_41PlVnwTbZuLeHsCq3)
• and I uploaded one too (I'd like to see it with our shirts on and off)
Nice to have
• Want it to be clean
• More gender neutral -- not overly masculine or femine
• I really like these book covers - so something similair woudl be great"
• Steady Steps: The 9-Week Meal Rhythm Method
• The Quiet Harvest Plan : Retune Your Habits for Gentle Fat Burning, Steady Vigor and Lasting Stamina
• Walk Far, Feel Light for Years

```html
<!DOCTYPE html>
<html lang="en">
<head>
<meta charset="utf-8">
<title>Summit Drive – Book Cover</title>
<link href="https://fonts.googleapis.com/css2?family=Bebas+Neue&family=Josefin+Sans:wght@400&family=Patrick+Hand&family=Open+Sans:wght@600&display=swap" rel="stylesheet">
<style>
  :root {
    --blue-deep: #0692cd;
    --blue-mid: #34a7d7;
    --blue-soft: #85cae6;
    --blue-pale: #cee9f5;
    --ink: #1c2136;
    --paper: #ffffff;
    --skin-light: #e9c7ae;
    --skin-warm: #d59f7f;
  }
  html, body {
    margin: 0;
    padding: 0;
    width: 890px;
    height: 1200px;
    overflow: hidden;
    background: var(--paper);
  }
  .cover {
    position: relative;
    width: 890px;
    height: 1200px;
    background: var(--paper);
    overflow: hidden;
  }
  .cover__authors {
    position: absolute;
    top: 56px;
    left: 0;
    width: 100%;
    text-align: center;
    font-family: "Josefin Sans", sans-serif;
    font-weight: 400;
    font-size: 58px;
    letter-spacing: 1px;
    color: var(--ink);
    margin: 0;
  }
  .cover__team {
    position: absolute;
    top: 136px;
    left: 0;
    width: 100%;
    text-align: center;
    font-family: "Patrick Hand", sans-serif;
    font-size: 34px;
    color: var(--ink);
    margin: 0;
  }
  .cover__photo {
    position: absolute;
    left: 250px;
    top: 240px;
    width: 500px;
    height: 920px;
    border-radius: 40px 40px 0 0;
    background: linear-gradient(180deg, var(--skin-light) 0%, var(--skin-warm) 45%, var(--blue-soft) 62%, var(--skin-light) 85%, var(--paper) 100%);
    opacity: 0.85;
  }
  .cover__headline {
    position: absolute;
    left: 0;
    top: 540px;
    width: 100%;
  }
  .cover__title {
    margin: 0 0 0 48px;
    font-family: "Bebas Neue", sans-serif;
    font-weight: 400;
    font-size: 250px;
    line-height: 0.84;
    color: var(--blue-deep);
    letter-spacing: 2px;
  }
  .cover__subtitle-band {
    margin-top: 34px;
    width: 850px;
    height: 48px;
    background: var(--blue-mid);
    display: flex;
    align-items: center;
    padding-left: 48px;
    box-sizing: border-box;
  }
  .cover__subtitle {
    margin: 0;
    font-family: "Open Sans", sans-serif;
    font-weight: 600;
    font-size: 22px;
    text-transform: uppercase;
    color: var(--paper);
    white-space: nowrap;
  }
</style>
</head>
<body>
  <main class="cover">
    <p class="cover__authors">DALE &amp; OWEN MERCER</p>
    <p class="cover__team">The father and the son fitness team</p>
    <div class="cover__photo" role="img" aria-label="Photo of father and son standing back to back, arms crossed, shirtless in board shorts"></div>
    <div class="cover__headline">
      <h1 class="cover__title">SUMMIT<br>DRIVE</h1>
      <div class="cover__subtitle-band">
        <p class="cover__subtitle">Push Past Your Limits, Find Strength Within Yourself</p>
      </div>
    </div>
  </main>
</body>
</html>
```